Brell Harbor Company Business Cards

Front and Back Business Card - logo and text setup - cool design. I need workable photoshop or illustrator files so I can setup each employee card with design that is created
Updates

Hi everyone, thank you for the great entries. Please no more white and blue cards - there are so many already - black and silver only now please. thanks!

Target Market(s)

Construction Industry - Facility Managers

Industry/Entity Type

Construction

Contact Information for Business Card

I really like contemporary simplistic looks - clean neat....not opposed to seeing some black backrounds

Requirements
Must have
• Logo/website address with design on front only - www.brellharbor-example.com (logo attached)
• Back:
• Name/Title/Company Address/Phone/email address
Nice to have
• Cool design
Should not have
• Nothing gimmicky like Fire or Water - since we are a Fire Protection company - it has all been done

```html
<!DOCTYPE html>
<html lang="en">
<head>
<meta charset="utf-8">
<title>Brell Harbor Company – Business Cards</title>
<link rel="stylesheet" href="https://fonts.googleapis.com/css2?family=Montserrat:wght@400;600;800&display=swap">
<style>
  :root {
    --backdrop: #e6e7e8;
    --card-white: #ffffff;
    --band-light: #ececed;
    --brand-black: #1d1e21;
    --brand-silver: #a9adb3;
    --silver-text: #7d8188;
    --shadow: rgba(0, 0, 0, 0.16);
  }
  html, body {
    margin: 0;
    width: 1200px;
    height: 969px;
    overflow: hidden;
    background: var(--backdrop);
    font-family: "Montserrat", Arial, sans-serif;
  }
  .card-sheet {
    position: relative;
    width: 1200px;
    height: 969px;
  }
  .card {
    position: absolute;
    top: 336px;
    width: 520px;
    height: 297px;
    box-shadow: 0 10px 26px var(--shadow);
    background: var(--card-white);
  }
  .card--front { left: 60px; }
  .card--back { left: 620px; }
  .card svg { display: block; }
  .fill-white { fill: var(--card-white); }
  .fill-light { fill: var(--band-light); }
  .fill-black { fill: var(--brand-black); }
  .fill-silver { fill: var(--brand-silver); }
  .logo-name { font-weight: 800; fill: var(--brand-black); }
  .front-web { font-weight: 400; font-size: 10.5px; fill: var(--silver-text); letter-spacing: 1px; }
  .person-name { font-weight: 600; font-size: 17px; fill: var(--brand-black); letter-spacing: 0.5px; }
  .person-title { font-weight: 400; font-size: 11px; fill: var(--silver-text); letter-spacing: 1px; }
  .contact-line { font-weight: 400; font-size: 10.5px; fill: var(--card-white); letter-spacing: 0.6px; }
  .icon { fill: var(--brand-black); }
  .icon-stroke { fill: none; stroke: var(--brand-black); stroke-width: 1.4; }
</style>
</head>
<body>
<main class="card-sheet">

  <section class="card card--front" aria-label="Business card front">
    <svg width="520" height="297" viewBox="0 0 520 297">
      <defs>
        <filter id="panel-shadow" x="-10%" y="-30%" width="120%" height="160%">
          <feDropShadow dx="0" dy="6" stdDeviation="7" flood-color="#000" flood-opacity="0.14"/>
        </filter>
      </defs>
      <rect class="fill-white" width="520" height="297"/>
      <polygon class="fill-light" points="0,95 140,0 230,0 0,150"/>
      <polygon class="fill-light" points="300,297 520,180 520,240 390,297"/>
      <polygon class="fill-black" points="330,0 520,0 520,205"/>
      <polygon class="fill-silver" points="0,150 235,297 150,297 0,205"/>
      <polygon class="fill-black" points="0,205 150,297 0,297"/>
      <rect class="fill-white" x="100" y="104" width="330" height="90" filter="url(#panel-shadow)"/>
      <text class="logo-name" x="265" y="148" font-size="23" text-anchor="middle">Brell Harbor Company</text>
      <text class="front-web" x="265" y="172" text-anchor="middle">WWW.BRELLHARBOR-EXAMPLE.COM</text>
    </svg>
  </section>

  <section class="card card--back" aria-label="Business card back">
    <svg width="520" height="297" viewBox="0 0 520 297">
      <rect class="fill-white" width="520" height="297"/>
      <polygon class="fill-light" points="110,0 155,0 255,297 210,297"/>
      <polygon class="fill-silver" points="155,0 200,0 300,297 255,297"/>
      <polygon class="fill-black" points="200,0 520,0 520,297 300,297"/>

      <g class="contact-icons">
        <rect class="fill-white" x="168" y="36" width="48" height="28"/>
        <rect class="icon-stroke" x="184" y="44" width="16" height="11"/>
        <polyline class="icon-stroke" points="184,44 192,51 200,44"/>

        <rect class="fill-white" x="188" y="96" width="48" height="28"/>
        <path class="icon" d="M206 102 l3 0 l2 4 l-2 2 q2 4 5 5 l2 -2 l4 2 l0 3 q-1 2 -3 2 q-10 -2 -13 -13 q0 -2 2 -3 z"/>

        <rect class="fill-white" x="208" y="156" width="48" height="28"/>
        <path class="icon" d="M232 162 a6 6 0 0 1 6 6 c0 5 -6 11 -6 11 c0 0 -6 -6 -6 -11 a6 6 0 0 1 6 -6 z"/>
        <circle class="fill-white" cx="232" cy="168" r="2.2"/>

        <rect class="fill-white" x="228" y="216" width="48" height="28"/>
        <circle class="icon-stroke" cx="252" cy="230" r="7"/>
        <ellipse class="icon-stroke" cx="252" cy="230" rx="3" ry="7"/>
        <line class="icon-stroke" x1="245" y1="230" x2="259" y2="230"/>
      </g>

      <text class="contact-line" x="232" y="54">OFFICE@BRELLHARBOR-EXAMPLE.COM</text>
      <text class="contact-line" x="252" y="114">+00 123 456 789</text>
      <text class="contact-line" x="272" y="174">ADDRESS GOES HERE</text>
      <text class="contact-line" x="292" y="234">WWW.BRELLHARBOR-EXAMPLE.COM</text>

      <text class="person-name" x="26" y="176">NAME SURNAME</text>
      <text class="person-title" x="158" y="191" text-anchor="end">MANAGER</text>

      <text class="logo-name" x="26" y="262" font-size="13">Brell Harbor Company</text>
    </svg>
  </section>

</main>
</body>
</html>
```